Postcard Design

Vantora Systems is the single source which provides audio visual technology solutions. we will undoubtedly save you time and will cut Audio visual cost dramatically. We provide the technology for your Large scale meetings, Events, Trade shows, product launches Pharma roll-outs nationwide. we customize online order form to customize your needs and save you time.

our motto; Raising the standards in service to our clients

Industry/Entity Type

Trade

```html
<!DOCTYPE html>
<html lang="en">
<head>
<meta charset="utf-8">
<title>Vantora Systems Postcard</title>
<link rel="stylesheet" href="https://fonts.googleapis.com/css2?family=EB+Garamond:wght@400;600;700&display=swap">
<style>
:root{
  --backdrop:#e8e4de;
  --card:#ffffff;
  --ink:#1e1e1e;
  --gold:#8a6a2c;
  --rule:#b9b9b9;
  --photo-deep:#0f3a3c;
  --photo-mid:#2f8f86;
  --photo-light:#a9d6cf;
  --photo-grey:#8d9a98;
}
*{margin:0;padding:0;box-sizing:border-box}
html,body{width:1200px;height:857px;overflow:hidden;background:var(--backdrop)}
body{position:relative;font-family:"EB Garamond",Garamond,serif;color:var(--ink)}
.postcard{position:absolute;width:466px;height:361px;background:var(--card);box-shadow:0 4px 14px rgba(0,0,0,.22);overflow:hidden}
.postcard--front{left:120px;top:199px}
.postcard--back{left:607px;top:312px}

.front__photo{position:absolute;inset:0;background:
  radial-gradient(ellipse at 30% 70%,var(--photo-light) 0%,transparent 40%),
  linear-gradient(160deg,var(--photo-deep) 0%,var(--photo-mid) 45%,var(--photo-grey) 75%,var(--photo-deep) 100%)}
.front__tagline{position:absolute;left:34px;top:50px;color:#fff;font-size:19px;line-height:22px}
.front__tagline .light{display:block;font-weight:400;opacity:.9}
.front__tagline .strong{display:block;padding-left:38px;font-weight:600}
.front__brand{position:absolute;left:296px;top:40px;width:158px;text-align:center;color:#fff;font-size:30px;font-weight:600;line-height:32px}

.back__services{position:absolute;left:12px;top:30px;width:215px;font-size:9.6px;line-height:12.6px}
.back__heading{color:var(--gold);font-weight:700;font-size:10px}
.back__list{list-style:none}
.back__list li::before{content:"• "}
.back__products{position:absolute;left:12px;top:164px;width:215px;font-size:9.6px;line-height:12.6px}
.back__columns{display:flex}
.back__columns .back__list{width:98px}
.back__contact{position:absolute;left:0;top:287px;width:232px;text-align:center}
.back__contact-label{font-size:9px;letter-spacing:.2px}
.back__contact-line{color:var(--gold);font-weight:700;font-size:12px;line-height:16px}
.back__divider{position:absolute;left:232px;top:17px;width:1px;height:322px;background:var(--rule)}
.back__brand{position:absolute;left:249px;top:28px;width:110px;font-size:21px;font-weight:600;line-height:22px;color:var(--ink)}
.back__address{position:absolute;left:249px;top:104px;font-size:9.6px;line-height:11.4px}
.back__address .name{color:var(--gold);font-weight:700;font-size:10px}
.back__stamp{position:absolute;left:405px;top:24px;width:48px;height:58px;border:1px solid var(--ink)}
.back__mail-lines{position:absolute;left:247px;top:200px;width:205px;height:85px}
</style>
</head>
<body>
<section class="postcard postcard--front">
  <div class="front__photo" role="img" aria-label="Close-up photograph of audio mixing console faders in teal light"></div>
  <p class="front__tagline"><span class="light">Raising the standards</span><span class="strong">in service to our clients</span></p>
  <p class="front__brand">Vantora Systems</p>
</section>

<section class="postcard postcard--back">
  <div class="back__services">
    <h2 class="back__heading">Our Services:</h2>
    <ul class="back__list">
      <li>Dinner Meetings (CME &amp; Product Launches)</li>
      <li>Large Scale Meetings &amp; Events</li>
      <li>Tradeshows &amp; Conferences</li>
      <li>Training Programs</li>
      <li>Corporations &amp; Small Businesses</li>
      <li>Meeting &amp; Event Planning Companies</li>
      <li>Associations, Foundations &amp; Societies</li>
      <li>Production Companies</li>
      <li>Hotel Properties</li>
    </ul>
  </div>
  <div class="back__products">
    <h2 class="back__heading">Our Products:</h2>
    <div class="back__columns">
      <ul class="back__list">
        <li>LCD Projectors</li>
        <li>Flat Panel Monitors</li>
        <li>Desktop Computers</li>
        <li>Printers &amp; Faxes</li>
        <li>Pipe &amp; Drape</li>
        <li>Projection Screens</li>
        <li>Copiers, Kiosks</li>
      </ul>
      <ul class="back__list">
        <li>Plasma Displays</li>
        <li>Complete Sound Packages</li>
        <li>Lighting &amp; Truss Systems</li>
        <li>Technicians For Hire</li>
        <li>ARS Systems</li>
        <li>Audio/Video Taping</li>
        <li>Laptop Computers</li>
      </ul>
    </div>
  </div>
  <div class="back__contact">
    <p class="back__contact-label">FOR MORE INFORMATION, PLEASE CONTACT:</p>
    <p class="back__contact-line">866-555-0142</p>
    <p class="back__contact-line">info@vantorasys-inc.com</p>
  </div>
  <div class="back__divider"></div>
  <p class="back__brand">Vantora Systems</p>
  <address class="back__address" style="font-style:normal">
    <span class="name">Vantora Systems</span><br>
    Corporate Office<br>
    2150 Alder Street<br>
    Milford, PA 18337<br>
    Toll free: 866-555-0142
  </address>
  <div class="back__stamp"></div>
  <svg class="back__mail-lines" viewBox="0 0 205 85" aria-hidden="true">
    <g stroke="#b9b9b9" stroke-width="1">
      <line x1="0" y1="0.5" x2="205" y2="0.5"/>
      <line x1="0" y1="21.5" x2="205" y2="21.5"/>
      <line x1="0" y1="42.5" x2="205" y2="42.5"/>
      <line x1="0" y1="63.5" x2="205" y2="63.5"/>
      <line x1="0" y1="84.5" x2="205" y2="84.5"/>
    </g>
  </svg>
</section>
</body>
</html>
```